mobile auto services

hello! we are an established company called "PLW Mechanics LTD" which provide car repairs on our premises. we need a flyer design for a new activity that is mobile and address to trade customers(independent garages and car sales)for specialist services (where usually they have to approach main dealers) like:
1-car keys lost and spares car key for most makes and mokels (out line the benefit of having a spare key for an emergency situation and convenience of using our service in case of a lost key. a spare key is most of the time cheaper than a lost one)
2-ecu's programming, coding, adaptation- most cars require programming after replacing any electronic control units or parts
3-software updates- on new models krd,valtrino,tz,ruxo there are very often software updates to improve functionality of ecu's.
4-dpf removal- software diesel vehicles starting with 2000-on have been fitted from factory with a diesel particulate filter (dpf) which in time gets clogged and cause running issues. we can disable the function from engine ecu, this way saving the cost of replacing.(physical removal of ceramic element has to be carried out by garage)
makes that we are covering for software at dealer level ruxo, tz, dorn, quelm, krd, valtrino, fendal, fell marten, talvine, morvane, baldrix, silvane, yarl, hesumi, dalvek.
the design should out line the services and customer benefit (cost and convenience) to use our services

Target Market(s)

independent garages and car traders

Industry/Entity Type

Electronic

Requirements
Must have
• i think it may look good to have car key pictures and some pictures suggesting ecu programming.

```html
<!DOCTYPE html>
<html lang="en">
<head>
<meta charset="utf-8">
<title>PLW Mechanics LTD – Mobile Auto Services Flyer</title>
<link rel="stylesheet" href="https://fonts.googleapis.com/css2?family=Alfa+Slab+One&family=Arvo:wght@700&family=Roboto+Condensed:ital,wght@0,400;0,700;1,400&display=swap">
<style>
  :root {
    --orange: #f07d1a;
    --blue: #1b75c9;
    --ink: #111111;
    --text: #2a2a2a;
    --paper: #ffffff;
    --backdrop: #e9e9e9;
    --photo-grey: #c9ccd0;
    --photo-dark: #4a5058;
    --photo-green: #3f6b45;
  }
  * { box-sizing: border-box; margin: 0; padding: 0; }
  html, body { width: 1200px; height: 1000px; overflow: hidden; }
  body { background: var(--backdrop); position: relative; font-family: "Roboto Condensed", Arial, sans-serif; color: var(--text); }

  .sheet { position: absolute; background: var(--paper); box-shadow: 0 2px 8px rgba(0,0,0,.15); overflow: hidden; }
  .sheet--front { left: 12px; top: 65px; width: 578px; height: 812px; }
  .sheet--back { left: 607px; top: 96px; width: 576px; height: 812px; }

  .slab { font-family: "Alfa Slab One", Georgia, serif; font-weight: 400; }
  .headline { position: absolute; left: 34px; top: 38px; color: var(--orange); font-size: 70px; line-height: 80px; letter-spacing: 0.5px; }
  .subhead { position: absolute; left: 34px; top: 304px; color: var(--ink); font-size: 28px; line-height: 40px; }
  .services-title { position: absolute; left: 34px; top: 472px; color: var(--blue); font-size: 21px; line-height: 26px; }
  .services-list { position: absolute; left: 34px; top: 508px; width: 300px; font-style: italic; font-size: 12.5px; line-height: 16px; text-transform: uppercase; color: var(--ink); }
  .intro { position: absolute; left: 34px; top: 552px; width: 305px; font-size: 10px; line-height: 13px; color: var(--ink); }
  .intro p + p { margin-top: 9px; }

  .product-photo { position: absolute; background: linear-gradient(160deg, var(--photo-grey), var(--photo-dark)); border-radius: 14px; }
  .product-photo--fob-a { left: 318px; top: 262px; width: 250px; height: 100px; }
  .product-photo--fob-b { left: 350px; top: 470px; width: 220px; height: 100px; }
  .product-photo--flip { left: 350px; top: 585px; width: 220px; height: 215px; z-index: 2; }

  .call-band { position: absolute; left: 0; width: 100%; background: var(--orange); color: #fff; font-style: italic; }
  .sheet--front .call-band { top: 643px; height: 52px; padding: 8px 0 0 34px; font-size: 13px; line-height: 17px; }

  .brand { position: absolute; display: flex; align-items: center; gap: 8px; }
  .brand-dot { width: 58px; height: 58px; border-radius: 50%; background: var(--blue); }
  .brand-name { font-family: "Arvo", Georgia, serif; font-weight: 700; color: var(--orange); font-size: 15px; text-transform: uppercase; }
  .tel { font-family: "Arvo", Georgia, serif; font-weight: 700; color: var(--blue); }
  .mobile { font-family: "Arvo", Georgia, serif; font-weight: 700; color: var(--ink); font-size: 13px; }
  .sheet--front .brand { left: 34px; top: 705px; }
  .sheet--front .tel { position: absolute; left: 104px; top: 742px; font-size: 23px; }
  .sheet--front .mobile { position: absolute; left: 104px; top: 775px; }

  /* back page */
  .section-bar { position: absolute; left: 0; width: 576px; height: 27px; background: var(--orange); color: #fff; font-family: "Arvo", Georgia, serif; font-weight: 700; font-size: 16px; padding: 3px 0 0 28px; }
  .lede { position: absolute; left: 28px; font-style: italic; font-size: 11px; line-height: 14px; color: var(--ink); width: 305px; }
  .ticks { position: absolute; left: 28px; list-style: none; font-size: 10.5px; line-height: 16px; width: 310px; color: var(--ink); }
  .ticks li::before { content: ""; display: inline-block; width: 9px; height: 9px; background: var(--blue); margin-right: 7px; vertical-align: -1px; }
  .ticks .sq { display: inline-block; width: 9px; height: 9px; background: var(--blue); margin: 0 4px; vertical-align: -1px; }

  .work-photo { position: absolute; left: 341px; width: 214px; z-index: 2; }
  .work-photo--cutter { top: 30px; height: 98px; background: linear-gradient(180deg, #e7e5e1, #a8a6a2); }
  .work-photo--board { top: 180px; height: 160px; background: linear-gradient(150deg, var(--photo-dark), var(--photo-green)); }
  .work-photo--engine { top: 360px; height: 135px; background: linear-gradient(170deg, #8e9399, #1e2126); }

  .onsite-badge { position: absolute; left: 264px; top: 425px; width: 130px; height: 88px; border-radius: 50%; background: var(--blue); border: 2px solid #fff; color: #fff; font-style: italic; font-size: 10.5px; line-height: 13px; text-align: center; padding-top: 17px; z-index: 3; }

  .makes-title { position: absolute; left: 28px; top: 528px; font-style: italic; font-size: 11px; color: var(--ink); }
  .makes { position: absolute; left: 20px; top: 560px; width: 540px; display: grid; grid-template-columns: repeat(8, 1fr); row-gap: 28px; align-items: center; text-align: center; }
  .make { font-weight: 700; font-size: 11.5px; text-transform: uppercase; color: var(--ink); line-height: 14px; }
  .make--red { color: #c8102e; }
  .make--blue { color: #1a4d9c; }
  .make--green { color: #2f7d3a; }

  .sheet--back .call-band { top: 672px; height: 32px; text-align: center; font-size: 13px; padding-top: 7px; }
  .sheet--back .brand { left: 22px; top: 723px; }
  .sheet--back .brand-name { font-size: 16px; }
  .contact { position: absolute; left: 283px; top: 708px; }
  .contact .tel { font-size: 21px; line-height: 26px; }
  .contact .mobile { line-height: 18px; }
  .contact .email { font-family: "Arvo", Georgia, serif; font-weight: 700; font-size: 11px; color: var(--ink); line-height: 16px; }
  .contact .web { font-family: "Arvo", Georgia, serif; font-weight: 700; font-size: 17px; color: var(--orange); line-height: 22px; }
</style>
</head>
<body>

<section class="sheet sheet--front">
  <h1 class="headline slab">Save time<br>&amp; increase<br>profits!</h1>
  <div class="product-photo product-photo--fob-a" role="img" aria-label="Photo of a silver and black smart car key fob"></div>
  <div class="product-photo product-photo--fob-b" role="img" aria-label="Photo of a black and silver slide car key fob"></div>
  <div class="product-photo product-photo--flip" role="img" aria-label="Photo of a black flip-out remote car key"></div>

  <h2 class="subhead slab">With our<br>Advanced<br>Diagnostics and<br>Car Key Services</h2>
  <h3 class="services-title slab">Our services:</h3>
  <p class="services-list">Lost and spare car keys, ECU programming,<br>software updates &amp; DPF removal and regeneration</p>
  <div class="intro">
    <p>We provide specialist services for independent garages, car dealerships and anyone in the motor trade so that you can save the expense, time and inconvenience of approaching the main dealers.</p>
    <p>We are fully equipped with Main Dealer Level equipment and have outstanding technicians all fully qualified and trained to achieve the best of their potential.</p>
  </div>

  <div class="call-band">Call now for more information, to speak to a representative,<br>or to book an appointment!</div>

  <div class="brand"><span class="brand-dot"></span><span class="brand-name">PLW Mechanics LTD</span></div>
  <div class="tel">Tel: 03300 482917</div>
  <div class="mobile">Mobile: 07700 900415</div>
</section>

<section class="sheet sheet--back">
  <h2 class="section-bar" style="top:22px">Lost or Spare Car Keys</h2>
  <div class="work-photo work-photo--cutter" role="img" aria-label="Photo of a key cutting machine at work"></div>
  <p class="lede" style="top:56px">We supply almost any vehicle manufacture car key</p>
  <ul class="ticks" style="top:74px">
    <li>We program new keys for most makes and models</li>
    <li>We can remove lost keys from a car's memory</li>
    <li>A spare key is cheaper than a replacement for the customer,<br>&nbsp;&nbsp;&nbsp;&nbsp;and an additional revenue stream for you</li>
  </ul>

  <h2 class="section-bar" style="top:145px">ECU Programming</h2>
  <div class="work-photo work-photo--board" role="img" aria-label="Photo of an electronic control unit circuit board being programmed"></div>
  <p class="lede" style="top:180px">We offer a wide range of programming, coding &amp; adaptation for various vehicle manufacturers. Just a few examples:</p>
  <ul class="ticks" style="top:214px">
    <li>Programming new electronic control unit</li>
    <li>Reprogram old electronic control unit<span class="sq"></span>Basic settings</li>
    <li>Code control control units<span class="sq"></span>Adapt steering column lock</li>
    <li>Automatic gearbox adaptation<span class="sq"></span>Retrofits<span class="sq"></span>SCN coding</li>
    <li>Ignition switch programming<span class="sq"></span>Remapping</li>
    <li>Remove component protection<span class="sq"></span>Software updates</li>
    <li>Remove or install speed limiter</li>
  </ul>
  <p class="lede" style="top:335px">Everything done on site, at your convenience</p>

  <h2 class="section-bar" style="top:358px">DPF Removal or Regeneration</h2>
  <div class="work-photo work-photo--engine" role="img" aria-label="Photo of a diagnostic tablet connected to a car with open bonnet"></div>
  <ul class="ticks" style="top:394px">
    <li>DPF Regeneration</li>
    <li>Disable the DPF from engine ECU</li>
    <li>Save cost of replacing the filter</li>
  </ul>

  <h2 class="section-bar" style="top:450px">Software Updates</h2>
  <div class="onsite-badge">All of our<br>services can be performed<br>on site, as well as<br>at our premises.</div>
  <ul class="ticks" style="top:486px">
    <li>Bring cars up to the latest, safest, software version</li>
    <li>Improve ECU functionality and remove bugs</li>
  </ul>

  <p class="makes-title">Makes we cover for software at dealer level:</p>
  <div class="makes">
    <span class="make make--green">Fell Marten</span>
    <span class="make">Valtrino</span>
    <span class="make make--red">Ruxo</span>
    <span class="make">KRD</span>
    <span class="make">Morvane</span>
    <span class="make make--blue">Yarl</span>
    <span class="make">Talvine</span>
    <span class="make make--red">Baldrix</span>
    <span class="make make--red">Grenmoor</span>
    <span class="make make--blue">TZ</span>
    <span class="make">Quelm<br><span class="make--red">Dalvek</span></span>
    <span class="make make--red">Hesumi<br><span style="color:var(--ink)">Silvane</span></span>
    <span class="make make--red">Dorn</span>
    <span class="make">Fendal</span>
    <span class="make">Hadrel</span>
  </div>

  <div class="call-band">Call now for more information, to speak to a representative, or to book an appointment!</div>

  <div class="brand"><span class="brand-dot"></span><span class="brand-name">PLW Mechanics LTD</span></div>
  <div class="contact">
    <div class="tel">Tel: 03300 482917</div>
    <div class="mobile">Mobile: 07700 900415</div>
    <div class="email">E-mail: sales@plwmechanics.example</div>
    <div class="web">www.plwmechanics.example</div>
  </div>
</section>

</body>
</html>
```